Mark & Lisa's Hammock Season Party

Invitation to a party 60-80 people at a private residence. Age range 30-40s.

Themes: summer/casual/Australian backyard/local community

**For delivery via both email and printed copy**
Would like one document suitable for both purposes or two versions for electronic or paper invitation. I will arrange printing so please prepare it in a suitable format.

Specimen text attached. Address and phone contact to follow by message with successful bidder

Thanks!
Mark

Target Market(s)

Locals, friends. Party attendees will typicaly be parents in their forties who who be leaving the kids at home for a relaxed party night, and walking home afterward

Industry/Entity Type

Community

Font styles to use
Sans Serif

Requirements
Should not have
• Cliche Australiana imagery. No kangaroos etc

```html
<!DOCTYPE html>
<html lang="en">
<head>
<meta charset="utf-8">
<title>Mark &amp; Lisa's Hammock Season Party – Details</title>
<link rel="stylesheet" href="https://fonts.googleapis.com/css2?family=Lato:wght@700&family=Raleway:wght@300&display=swap">
<style>
  :root {
    --night: #12112f;
    --ink-strong: #ffffff;
    --ink-soft: #c9c9d8;
    --rule: #b9b9c9;
  }
  * { margin: 0; padding: 0; box-sizing: border-box; }
  html, body { width: 857px; height: 1200px; overflow: hidden; background: var(--night); }
  .invite-back {
    position: relative;
    width: 857px;
    height: 1200px;
    background: var(--night);
    color: var(--ink-soft);
    font-family: "Raleway", "Helvetica Neue", Arial, sans-serif;
    font-weight: 300;
  }
  .details-card {
    position: absolute;
    left: 173px; top: 241px;
    width: 511px; height: 309px;
    border: 1px solid var(--rule);
  }
  .details-list { position: absolute; left: 90px; width: 329px; top: 0; list-style: none; }
  .detail-row {
    height: 44px;
    display: flex; align-items: center; justify-content: center;
    border-bottom: 1px solid var(--rule);
    font-size: 17px; letter-spacing: 0.2px;
  }
  .detail-row:first-child { height: 40px; }
  .detail-row:last-child { border-bottom: none; }
  .detail-row--heading {
    font-family: "Lato", "Helvetica Neue", Arial, sans-serif;
    font-weight: 700;
    color: var(--ink-strong);
    font-size: 17.5px;
  }
  .contact-card {
    position: absolute;
    left: 168px; top: 628px;
    width: 521px; height: 157px;
    border: 1px solid var(--rule);
    border-top: none;
  }
  .contact-card::before, .contact-card::after {
    content: ""; position: absolute; top: 0; height: 1px; background: var(--rule);
  }
  .contact-card::before { left: 0; width: 191px; }
  .contact-card::after { right: 0; width: 205px; }
  .contact-icon { position: absolute; left: 223px; top: -40px; width: 76px; height: 84px; }
  .contact-prompt {
    position: absolute; top: 58px; left: 0; width: 100%;
    text-align: center; font-size: 17px;
  }
  .contact-rule { position: absolute; left: 63px; top: 92px; width: 395px; height: 1px; background: var(--rule); }
  .contact-numbers {
    position: absolute; top: 111px; left: 0; width: 100%;
    text-align: center; font-size: 17px; white-space: pre;
  }
  .friends-note {
    position: absolute; left: 0; top: 876px; width: 857px;
    text-align: center; font-size: 17px; line-height: 22.5px;
  }
</style>
</head>
<body>
<main class="invite-back">
  <section class="details-card">
    <ul class="details-list">
      <li class="detail-row detail-row--heading">Child-free event</li>
      <li class="detail-row detail-row--heading">DRESS</li>
      <li class="detail-row">summer casual, bare feet welcome</li>
      <li class="detail-row detail-row--heading">Cocktail food provided</li>
      <li class="detail-row">BYO but only if you insist</li>
      <li class="detail-row detail-row--heading">RSVP</li>
      <li class="detail-row">for catering would be nice.</li>
    </ul>
  </section>

  <section class="contact-card">
    <svg class="contact-icon" viewBox="0 0 76 84" aria-hidden="true">
      <rect x="2" y="0" width="40" height="60" rx="5" fill="#fff"/>
      <rect x="7" y="8" width="30" height="40" fill="#12112f"/>
      <rect x="16" y="3" width="12" height="2" rx="1" fill="#12112f"/>
      <circle cx="22" cy="54" r="3" fill="#12112f"/>
      <path d="M42 26 C50 28 54 34 52 40 L64 44 L76 56 L62 83 L56 80 C46 78 34 74 20 70 L22 62 C30 64 36 64 42 62 Z" fill="#fff"/>
      <path d="M40 24 C48 26 50 32 46 38" stroke="#12112f" stroke-width="3" fill="none"/>
    </svg>
    <p class="contact-prompt">TEXT US before Xmas please.</p>
    <div class="contact-rule"></div>
    <p class="contact-numbers">Mark |  +971 000 12 34  or  Lisa | +971 000 43 21</p>
  </section>

  <p class="friends-note">If you have some friends or neighbours<br>that you like to hang out with, we would<br>love to meet. Bring them with you!</p>
</main>
</body>
</html>
```